Church Christmas Flyer

The flyer is to advertise our Christmas Eve services. The flyer is for a Christian church service to celebrate the birth of Jesus. We would like to see designs that use blue, silver and gold for colors but feel free to be creative. We are interested in a flyer that is has texture, depth and is more abstract than literal. Don't be afraid to layer. Please make the flyer double sided

* I uploaded our Christmas flyer from last year.

Target Market(s)

30-55 year old, male and female

Industry/Entity Type

Church

Requirements
Must have
• Map to the church
Church phone number 555-314-7096
Service times 3:00pm and 5:00pm
church address 28315 Marigold Ave, Pinecrest, Ca. 93999
church website www.brookstonefellowship.example
Scripture verse

Text must stand out and be easy to read
Nice to have
• Use of the star in the sky that guided the wise men to Jesus.
Should not have
• Santa Clause, Snowmen, Reindeer

```html
<!DOCTYPE html>
<html lang="en">
<head>
<meta charset="utf-8">
<title>Christmas Eve Flyer</title>
<link rel="stylesheet" href="https://fonts.googleapis.com/css2?family=Great+Vibes&family=Marcellus&display=swap">
<style>
:root{
  --page:#ffffff;
  --night-deep:#0b1a33;
  --night-mid:#16315a;
  --night-edge:#070d1a;
  --gold:#f3e6a6;
  --gold-strong:#e9cf6e;
  --cream:#fbf6dc;
  --silver:#e8ecf2;
  --map-base:#ecebe6;
  --map-road:#f2dc8a;
}
*{margin:0;padding:0;box-sizing:border-box}
html,body{width:1200px;height:1059px;overflow:hidden;background:var(--page)}
.canvas{position:relative;width:1200px;height:1059px}
.card{position:absolute;width:890px;height:420px;overflow:hidden;
  box-shadow:0 10px 22px rgba(0,0,0,.35)}
.card--front{left:100px;top:45px;
  background:radial-gradient(ellipse at 30% 40%,var(--night-mid) 0%,var(--night-deep) 55%,var(--night-edge) 100%)}
.card--back{left:125px;top:525px;
  background:radial-gradient(ellipse at 25% 45%,var(--night-mid) 0%,var(--night-deep) 60%,var(--night-edge) 100%)}
.sky-glow,.swoosh,.band{position:absolute;left:0;top:0}
.title{position:absolute;left:112px;top:40px;font-family:"Great Vibes",cursive;
  font-size:112px;line-height:1;color:var(--gold);letter-spacing:4px;white-space:nowrap;
  text-shadow:0 2px 4px rgba(0,0,0,.5)}
.tagline{position:absolute;left:330px;top:160px;font-family:"Great Vibes",cursive;
  font-size:60px;line-height:1;color:var(--silver);white-space:nowrap}
.verse{position:absolute;left:128px;top:322px;font-family:"Marcellus",serif;
  font-size:64px;line-height:1;color:var(--cream);white-space:nowrap;
  text-shadow:0 0 1px var(--cream),0 2px 4px rgba(0,0,0,.6)}
.details{position:absolute;left:30px;top:0;width:540px;height:420px;
  font-family:"Marcellus",serif;color:var(--gold)}
.details p{position:absolute;left:0;width:100%;text-align:center;white-space:nowrap;line-height:1}
.details .times{top:52px;font-size:22px}
.details .times strong{font-size:30px;font-weight:400}
.details .label{top:115px;font-size:22px}
.details .phone{top:155px;font-size:44px}
.details .web{top:240px;font-size:20px}
.details .addr1{top:280px;font-size:22px}
.details .address{top:315px;font-size:22px;color:var(--gold-strong)}
.map{position:absolute;left:595px;top:35px;width:240px;height:240px;
  transform:rotate(-18deg);
  background:linear-gradient(135deg,var(--map-base) 0%,#dedcd4 60%,var(--map-road) 100%);
  box-shadow:0 4px 10px rgba(0,0,0,.4)}
</style>
</head>
<body>
<main class="canvas">

  <section class="card card--front" aria-label="Flyer front">
    <svg class="sky-glow" width="890" height="420" aria-hidden="true">
      <defs>
        <radialGradient id="glow" cx="50%" cy="50%" r="50%">
          <stop offset="0" stop-color="#ffffff" stop-opacity=".25"/>
          <stop offset="1" stop-color="#ffffff" stop-opacity="0"/>
        </radialGradient>
      </defs>
      <ellipse cx="660" cy="210" rx="260" ry="90" fill="url(#glow)"/>
    </svg>
    <svg class="swoosh" width="890" height="420" aria-hidden="true" fill="none">
      <path d="M0 175 C180 160 260 210 400 250 C520 285 620 220 760 170 C820 150 860 148 890 150" stroke="#ffffff" stroke-width="2" opacity=".85"/>
      <path d="M0 185 C170 180 250 235 380 275 C470 300 560 300 660 300 C700 302 740 305 760 310" stroke="var(--gold-strong)" stroke-width="2"/>
      <path d="M0 195 C160 195 240 240 360 270 C460 292 560 270 650 260" stroke="#9aa8c0" stroke-width="1.5"/>
      <path d="M340 130 C480 120 620 140 720 110 C800 90 860 110 890 125" stroke="#ffffff" stroke-width="1.5" opacity=".7"/>
    </svg>
    <h1 class="title">Christmas Eve</h1>
    <p class="tagline">A celebration of God's love</p>
    <p class="verse">Scripture verse</p>
  </section>

  <section class="card card--back" aria-label="Flyer back">
    <svg class="band" width="890" height="420" aria-hidden="true">
      <defs>
        <linearGradient id="bandTop" x1="0" y1="0" x2="0" y2="1">
          <stop offset="0" stop-color="#ffffff"/>
          <stop offset="1" stop-color="#f1df93"/>
        </linearGradient>
        <linearGradient id="bandBottom" x1="0" y1="0" x2="0" y2="1">
          <stop offset="0" stop-color="#f1df93"/>
          <stop offset="1" stop-color="#ffffff"/>
        </linearGradient>
      </defs>
      <path d="M0 0 H890 V30 C720 20 560 60 380 48 C220 38 100 48 0 60 Z" fill="url(#bandTop)"/>
      <path d="M0 395 C200 380 420 370 600 368 C740 366 830 355 890 345 V420 H0 Z" fill="url(#bandBottom)"/>
    </svg>
    <div class="details">
      <p class="times">Service times <strong>3:00pm</strong> and <strong>5:00pm</strong></p>
      <p class="label">Church phone number</p>
      <p class="phone">555-314-7096</p>
      <p class="web">church website www.brookstonefellowship.example</p>
      <p class="addr1">church address 28315</p>
      <p class="address">Marigold Ave, Pinecrest, Ca. 93999</p>
    </div>
    <div class="map" role="img" aria-label="Street map showing the church location"></div>
  </section>

</main>
</body>
</html>
```